Startup of Management Company looking for Designers!

I am looking for an upscale website. Valmoreth will focus on Real Estate, Wealth Management, and Consulting,

Target Market(s)

investors, sellers of real estate, people looking to have their real estate management.
companies looking for consulting services

Number of Pages Required

5+ page

Font styles to use
Sans Serif

Requirements
Must have
• pictures, real.

```html
<!DOCTYPE html>
<html lang="en">
<head>
<meta charset="utf-8">
<title>Valmoreth — Real Estate Management</title>
<link href="https://fonts.googleapis.com/css2?family=Open+Sans:wdth,wght@75,600;75,700;100,400&family=Lato:wght@400;700&display=swap" rel="stylesheet">
<style>
:root{
  --ink:#111;
  --teal:#1aa5a5;
  --mint:#e8f8f8;
  --white:#fff;
  --body:#333;
  --dark:#283034;
  --night:#2b2a2c;
}
*{margin:0;padding:0;box-sizing:border-box}
html,body{width:1200px;height:5046px;overflow:hidden;background:var(--white)}
body{position:relative;font-family:"Lato",sans-serif;color:var(--body)}
.abs{position:absolute}
.cond{font-family:"Open Sans",sans-serif;font-stretch:75%;font-weight:700;color:var(--ink)}
.text{font-size:13.5px;line-height:24px;color:var(--body)}

/* header */
.site-header{position:absolute;top:0;left:0;width:1200px;height:88px;background:var(--white)}
.brand{position:absolute;left:112px;top:26px;font-family:"Open Sans",sans-serif;font-weight:600;font-size:28px;letter-spacing:1px;color:var(--ink)}
.nav a{position:absolute;top:36px;font-family:"Open Sans",sans-serif;font-stretch:75%;font-weight:700;font-size:14px;color:var(--ink);text-decoration:none}
.nav a.active{color:var(--teal)}

/* hero */
.hero{position:absolute;top:88px;left:0;width:1200px;height:553px;background:linear-gradient(180deg,#5a3a48 0%,#b0604a 28%,#6e4a3e 50%,#3d4a2c 72%,#4d5a3a 100%)}
.hero-title{position:absolute;left:112px;top:146px;font-size:50px;line-height:58px;color:var(--white)}
.hero-sub{position:absolute;left:112px;top:276px;font-size:14.5px;line-height:24px;color:var(--white)}
.btn-outline{position:absolute;left:112px;top:346px;width:150px;height:52px;border:2px solid var(--white);color:var(--white);font-family:"Open Sans",sans-serif;font-stretch:75%;font-weight:700;font-size:14px;line-height:48px;text-align:center}

/* services */
.services{position:absolute;top:641px;left:0;width:1200px;height:1456px;background:var(--mint)}
.section-title{position:absolute;left:0;width:1200px;text-align:center;font-size:25px}
.photo{position:absolute}
.svc-title{position:absolute;font-size:60px;line-height:68px}
.svc-sub{position:absolute;font-family:"Open Sans",sans-serif;font-stretch:75%;font-weight:700;font-size:14.5px;color:var(--ink)}
.svc-body{position:absolute;width:320px}

/* investors */
.card{position:absolute;width:380px}
.card .photo{position:relative;width:380px;height:300px}
.card-kicker{margin-top:30px;font-size:13.5px}
.card-title{margin-top:18px;font-size:21px}
.rule{width:80px;height:2px;background:var(--ink);margin-top:6px}
.card .text{margin-top:14px;width:330px}
.price{margin-top:12px;font-family:"Open Sans",sans-serif;font-stretch:75%;font-weight:700;font-size:19px;color:var(--teal)}
.card-inner{padding-left:2px}

/* features */
.tile{position:absolute;width:380px;height:325px}
.tile.mint{background:var(--mint)}
.feature{position:absolute}
.feature h3{margin-top:16px;font-size:23px;line-height:29px}
.feature .rule{margin-top:12px;width:84px}
.feature .text{margin-top:14px;width:260px;font-size:13px;line-height:22px}

/* testimonials */
.testimonials{position:absolute;top:4208px;left:0;width:1200px;height:472px;background:linear-gradient(180deg,#2a2628 0%,#3c3430 45%,#2c302e 100%)}
.testimonials .section-title{color:var(--white);top:120px}
.quote{position:absolute;top:246px;width:250px;text-align:center;font-size:13px;line-height:22px;color:var(--white)}
.quote cite{display:block;margin-top:20px;font-style:normal;font-family:"Open Sans",sans-serif;font-stretch:75%;font-weight:700;font-size:14px;color:var(--teal)}

/* footer */
.site-footer{position:absolute;top:4680px;left:0;width:1200px;height:366px;background:var(--dark);color:var(--white)}
.footer-head{position:absolute;font-family:"Open Sans",sans-serif;font-stretch:75%;font-weight:700;font-size:13px;line-height:22px;color:var(--white)}
.footer-text{position:absolute;font-size:13px;line-height:26px;color:var(--white)}
.field{position:absolute;border:1px solid #8a9398;font-size:13px;color:var(--white);padding:6px 14px}
.submit{position:absolute;left:977px;top:278px;font-family:"Open Sans",sans-serif;font-stretch:75%;font-weight:700;font-size:14px;color:var(--white)}
</style>
</head>
<body>

<header class="site-header">
  <div class="brand">VALMORETH</div>
  <nav class="nav">
    <a class="active" style="left:620px" href="#">HOME</a>
    <a style="left:707px" href="#">ABOUT US</a>
    <a style="left:816px" href="#">SERVICES</a>
    <a style="left:918px" href="#">CONTACT</a>
  </nav>
</header>

<section class="hero" role="img" aria-label="Suburban neighbourhood of large brick houses at sunset under a pink and orange sky">
  <h1 class="hero-title cond">REAL ESTATE<br>MANAGEMENT</h1>
  <p class="hero-sub">Sed ut perspiciatis unde omnis iste natus error sit<br>voluptatem accusantium doloremque laudantium.</p>
  <div class="btn-outline">LEARN MORE</div>
</section>

<section class="services">
  <h2 class="section-title cond" style="top:82px">SED UT PERSPICIATIS</h2>

  <div class="photo" style="left:280px;top:160px;width:292px;height:368px;background:linear-gradient(135deg,#5a3320 0%,#c86a30 50%,#f0a040 100%)" role="img" aria-label="Hand holding a small model house"></div>
  <h3 class="svc-title cond" style="left:609px;top:200px">REAL<br>ESTATE</h3>
  <div class="svc-sub" style="left:612px;top:352px">Sed ut perspiciatis</div>
  <p class="svc-body text" style="left:614px;top:383px">Lorem ipsum dolor sit amet, consectetur adipiscing elit, sed do eiusmod tempor incididunt ut labore et dolore magna aliqua. Ut enim ad minim veniam, quis nostrud exercitation</p>

  <h3 class="svc-title cond" style="left:327px;top:618px">WEALTH<br>MANAGEMENT</h3>
  <div class="svc-sub" style="left:330px;top:772px">Sed ut perspiciatis</div>
  <p class="svc-body text" style="left:332px;top:803px">Lorem ipsum dolor sit amet, consectetur adipiscing elit, sed do eiusmod tempor incididunt ut labore et dolore magna aliqua. Ut enim ad minim veniam, quis nostrud exercitation</p>
  <div class="photo" style="left:705px;top:581px;width:293px;height:368px;background:linear-gradient(160deg,#8a8e92 0%,#3a4450 45%,#d8dadc 100%)" role="img" aria-label="Two businessmen reviewing financial charts at a desk"></div>

  <div class="photo" style="left:280px;top:1000px;width:292px;height:368px;background:linear-gradient(135deg,#c8a880 0%,#e8d8c8 40%,#3a5a88 100%)" role="img" aria-label="Couple meeting with an advisor over a laptop"></div>
  <h3 class="svc-title cond" style="left:609px;top:1070px">CONSULTING</h3>
  <div class="svc-sub" style="left:612px;top:1162px">Sed ut perspiciatis</div>
  <p class="svc-body text" style="left:614px;top:1193px">Lorem ipsum dolor sit amet, consectetur adipiscing elit, sed do eiusmod tempor incididunt ut labore et dolore magna aliqua. Ut enim ad minim veniam, quis nostrud exercitation</p>
</section>

<h2 class="section-title cond" style="top:2176px">VALMORETH&nbsp; INVESTORS</h2>

<article class="card" style="left:206px;top:2271px">
  <div class="photo" role="img" aria-label="Family meeting with an agent at a laptop" style="background:linear-gradient(135deg,#d8c8b0 0%,#8aa0c0 45%,#c04040 100%)"></div>
  <div class="card-inner">
    <div class="card-kicker cond">LOREM IPSUM</div>
    <h3 class="card-title cond">SED UT PERSPICIATIS</h3>
    <div class="rule"></div>
    <p class="text">Lorem ipsum dolor sit amet, consectetur adipiscing elit, sed do eiusmod tempor incididunt ut labore et dolore magna aliqua. Ut enim ad minim veniam, quis nostrud exercitation ullamco laboris nisi ut aliquip</p>
    <div class="price">$699.000</div>
  </div>
</article>
<article class="card" style="left:615px;top:2271px">
  <div class="photo" role="img" aria-label="Model house, keys and gavel on a desk" style="background:linear-gradient(135deg,#e8eef2 0%,#c8ccd0 50%,#8a6a40 100%)"></div>
  <div class="card-inner">
    <div class="card-kicker cond">LOREM IPSUM</div>
    <h3 class="card-title cond">SED UT PERSPICIATIS</h3>
    <div class="rule"></div>
    <p class="text">Lorem ipsum dolor sit amet, consectetur adipiscing elit, sed do eiusmod tempor incididunt ut labore et dolore magna aliqua. Ut enim ad minim veniam, quis nostrud exercitation ullamco laboris nisi ut aliquip</p>
    <div class="price">$699.000</div>
  </div>
</article>
<article class="card" style="left:206px;top:2845px">
  <div class="photo" role="img" aria-label="Calculator, coins and model buildings on a wooden table" style="background:linear-gradient(135deg,#b8a890 0%,#e8dcc8 50%,#c0a070 100%)"></div>
  <div class="card-inner">
    <div class="card-kicker cond">LOREM IPSUM</div>
    <h3 class="card-title cond">SED UT PERSPICIATIS</h3>
    <div class="rule"></div>
    <p class="text">Lorem ipsum dolor sit amet, consectetur adipiscing elit, sed do eiusmod tempor incididunt ut labore et dolore magna aliqua. Ut enim ad minim veniam, quis nostrud exercitation ullamco laboris nisi ut aliquip</p>
    <div class="price">$699.000</div>
  </div>
</article>
<article class="card" style="left:615px;top:2845px">
  <div class="photo" role="img" aria-label="Hand holding house keys against a soft green background" style="background:linear-gradient(160deg,#d8d0c0 0%,#a8a890 45%,#3a6a50 100%)"></div>
  <div class="card-inner">
    <div class="card-kicker cond">LOREM IPSUM</div>
    <h3 class="card-title cond">SED UT PERSPICIATIS</h3>
    <div class="rule"></div>
    <p class="text">Lorem ipsum dolor sit amet, consectetur adipiscing elit, sed do eiusmod tempor incididunt ut labore et dolore magna aliqua. Ut enim ad minim veniam, quis nostrud exercitation ullamco laboris nisi ut aliquip</p>
    <div class="price">$699.000</div>
  </div>
</article>

<section class="features">
  <div class="tile mint" style="left:206px;top:3468px"></div>
  <h2 class="cond abs" style="left:229px;top:3540px;font-size:52px;line-height:62px">LOREM IPSUM<br>DOLOR SIT AMET<br>CONSECTETUR</h2>

  <div class="feature" style="left:654px;top:3522px">
    <svg width="44" height="58" viewBox="0 0 44 58" fill="none" stroke="#1aa5a5" stroke-width="3"><rect x="3" y="7" width="38" height="48" rx="2"/><rect x="14" y="2" width="16" height="9" rx="2" fill="#fff"/><path d="M11 24h22M11 33h22M11 42h22"/></svg>
    <h3 class="cond">FREE REGISTRATION<br>NO HIDDEN FEES</h3>
    <div class="rule"></div>
    <p class="text">Lorem ipsum dolor sit amet, consectetur adipiscing elit, sed do</p>
  </div>

  <div class="feature" style="left:274px;top:3853px">
    <svg width="58" height="52" viewBox="0 0 58 52" fill="none" stroke="#1aa5a5" stroke-width="3" stroke-linejoin="round"><path d="M29 3 55 15 29 27 3 15Z"/><path d="M3 25l26 12 26-12"/><path d="M3 35l26 12 26-12"/></svg>
    <h3 class="cond">FREE PROPERTY<br>VALUATION</h3>
    <div class="rule"></div>
    <p class="text">Lorem ipsum dolor sit amet, consectetur adipiscing elit, sed do</p>
  </div>

  <div class="tile mint" style="left:585px;top:3793px"></div>
  <div class="feature" style="left:654px;top:3858px">
    <svg width="56" height="48" viewBox="0 0 56 48" fill="none" stroke="#1aa5a5" stroke-width="3" stroke-linejoin="round"><path d="M3 8 19 3 37 9 53 4V40L37 45 19 39 3 44Z"/><path d="M19 3v36M37 9v36"/></svg>
    <h3 class="cond">OFFICES IN 4<br>LOCATIONS</h3>
    <div class="rule"></div>
    <p class="text">Lorem ipsum dolor sit amet, consectetur adipiscing elit, sed do</p>
  </div>
</section>

<section class="testimonials" role="img" aria-label="Dusk view of a suburban street with houses, darkened">
  <h2 class="section-title cond">WHAT OUR CLIENTS THINK</h2>
  <blockquote class="quote" style="left:188px">“Sed ut perspiciatis unde omnis iste natus error sit voluptatem accusantium doloremque laudantium”<cite>MAREN HOLT</cite></blockquote>
  <blockquote class="quote" style="left:474px">“Sed ut perspiciatis unde omnis iste natus error sit voluptatem accusantium doloremque laudantium”<cite>MAREN HOLT</cite></blockquote>
  <blockquote class="quote" style="left:760px">“Sed ut perspiciatis unde omnis iste natus error sit voluptatem accusantium doloremque laudantium”<cite>MAREN HOLT</cite></blockquote>
</section>

<footer class="site-footer">
  <div class="footer-head" style="left:178px;top:82px">SED UT PERSPICIATIS UNDE OMNIS ISTE NATUS<br>ERROR SIT VOLUPTATEM:</div>
  <div class="footer-text" style="left:178px;top:144px">Phone: 555-010-2020<br>Email: hello@valmoreth.com<br>Fax: 555-010-3030</div>
  <div class="footer-text" style="left:400px;top:144px;line-height:22px">Lorem ipsum dolor sit amet<br>consectetur adipiscing elit</div>
  <div class="footer-text" style="left:176px;top:236px">©Copyrights 2021 Valmoreth &nbsp;|&nbsp; All Rights Reserved</div>

  <div class="footer-head" style="left:638px;top:82px">SED UT PERSPICIATIS UNDE OMNIS ISTE NATUS<br>ERROR SIT VOLUPTATEM:</div>
  <div class="field" style="left:638px;top:145px;width:186px;height:30px">Name</div>
  <div class="field" style="left:638px;top:189px;width:186px;height:30px">Email</div>
  <div class="field" style="left:638px;top:231px;width:186px;height:30px">Subject</div>
  <div class="field" style="left:838px;top:145px;width:186px;height:116px">Message</div>
  <div class="submit">SUBMIT</div>
</footer>

</body>
</html>
```